Cedar Pike seamless gutters and drains

I need a cool, modern, sleek design for t-380 crew cab trucks and 16’ box trucks. I’m not wanting full wraps but I want like a half wrap in the center of the vehicles. Blue background with white logo. With website and phone number only.

cedarpikeco.com
318.555.0147

Target Market(s)

Homeowners and contractors

Industry/Entity Type

Seamless gutters and drainage

Font styles to use
Sans Serif

Colors
0054AA
0677BA
7BADD7
CADEEF
E8F1F8

Requirements
Must have
• Blue background with white logo and white lettering
Nice to have
• Blue background with curvatures and white logo and lettering in the middle of the box truck and t-380’s

```html
<!DOCTYPE html>
<html lang="en">
<head>
<meta charset="utf-8">
<title>Cedar Pike – Vehicle Graphics</title>
<link href="https://fonts.googleapis.com/css2?family=Montserrat:wght@600;700&display=swap" rel="stylesheet">
<style>
  :root {
    --blue-deep: #0054AA;
    --blue-main: #0677BA;
    --blue-mid: #7BADD7;
    --blue-light: #CADEEF;
    --blue-pale: #E8F1F8;
    --white: #FFFFFF;
    --stage: #EEF1F4;
    --frame: #111111;
  }
  html, body {
    margin: 0;
    padding: 0;
    width: 762px;
    height: 1200px;
    overflow: hidden;
    background: var(--stage);
    font-family: "Montserrat", sans-serif;
  }
  .canvas {
    position: relative;
    width: 762px;
    height: 1200px;
  }
  .artwork {
    position: absolute;
    left: 31px;
    width: 700px;
    overflow: hidden;
  }
  .artwork--box-truck {
    top: 150px;
    height: 250px;
    background: var(--blue-main);
    border: 4px solid var(--frame);
    box-sizing: border-box;
  }
  .artwork--crew-cab {
    top: 640px;
    height: 300px;
    background: var(--white);
    box-shadow: 0 2px 10px rgba(0,0,0,0.12);
  }
  .artwork svg.backdrop {
    position: absolute;
    inset: 0;
  }
  .drops-art {
    position: absolute;
    border-radius: 40px;
    background: radial-gradient(circle at 40% 40%, var(--blue-light), var(--blue-mid) 60%, var(--blue-main));
    opacity: 0.9;
  }
  .artwork--box-truck .drops-art {
    left: 14px;
    top: 4px;
    width: 230px;
    height: 146px;
  }
  .artwork--crew-cab .drops-art {
    left: 500px;
    top: 90px;
    width: 180px;
    height: 160px;
    border-radius: 60px 60px 20px 20px;
  }
  .brand-name {
    position: absolute;
    margin: 0;
    color: var(--white);
    font-weight: 700;
    letter-spacing: 0.5px;
    white-space: nowrap;
    line-height: 1;
  }
  .artwork--box-truck .brand-name {
    left: 300px;
    top: 118px;
    font-size: 38px;
  }
  .artwork--crew-cab .brand-name {
    left: 260px;
    top: 120px;
    font-size: 30px;
  }
  .contact {
    position: absolute;
    margin: 0;
    padding: 0;
    list-style: none;
    color: var(--white);
    font-weight: 600;
  }
  .contact li {
    display: flex;
    align-items: center;
  }
  .contact svg { flex: none; }
  .artwork--box-truck .contact {
    left: 14px;
    top: 166px;
    font-size: 22px;
  }
  .artwork--box-truck .contact li { gap: 12px; height: 36px; }
  .artwork--crew-cab .contact {
    left: 238px;
    top: 170px;
    font-size: 14px;
  }
  .artwork--crew-cab .contact li { gap: 8px; height: 22px; }
</style>
</head>
<body>
<main class="canvas">

  <section class="artwork artwork--box-truck" aria-label="Box truck side graphic">
    <svg class="backdrop" width="692" height="242" viewBox="0 0 692 242" aria-hidden="true">
      <path d="M230 0 C 430 20, 650 80, 692 210 L692 0 Z" fill="var(--white)"/>
    </svg>
    <div class="drops-art" role="img" aria-label="Illustration of splashing blue water droplets"></div>
    <p class="brand-name">Cedar Pike</p>
    <ul class="contact">
      <li>
        <svg width="22" height="22" viewBox="0 0 22 22" aria-hidden="true">
          <rect x="1" y="1" width="20" height="20" fill="none" stroke="var(--white)" stroke-width="2"/>
          <path d="M7 5 l2 0 l1 3 l-1.5 1 a7 7 0 0 0 3.5 3.5 l1 -1.5 l3 1 l0 2 a2 2 0 0 1 -2 1.5 a10 10 0 0 1 -8.5 -8.5 a2 2 0 0 1 1.5 -2z" fill="var(--white)"/>
        </svg>
        <span>318.555.0147</span>
      </li>
      <li>
        <svg width="22" height="22" viewBox="0 0 22 22" aria-hidden="true">
          <rect x="1" y="1" width="20" height="20" fill="none" stroke="var(--white)" stroke-width="2"/>
          <circle cx="11" cy="11" r="6" fill="none" stroke="var(--white)" stroke-width="1.5"/>
          <ellipse cx="11" cy="11" rx="2.5" ry="6" fill="none" stroke="var(--white)" stroke-width="1.2"/>
          <line x1="5" y1="11" x2="17" y2="11" stroke="var(--white)" stroke-width="1.2"/>
        </svg>
        <span>cedarpikeco.com</span>
      </li>
    </ul>
  </section>

  <section class="artwork artwork--crew-cab" aria-label="Crew cab truck side graphic">
    <svg class="backdrop" width="700" height="300" viewBox="0 0 700 300" aria-hidden="true">
      <path d="M0 300 L0 270 C 120 210, 200 140, 230 60 L700 60 L700 300 Z" fill="var(--blue-main)"/>
      <path d="M440 60 C 520 40, 620 40, 700 70 L700 60 Z" fill="var(--blue-deep)" opacity="0.4"/>
    </svg>
    <div class="drops-art" role="img" aria-label="Illustration of large blue water droplets across the front fender"></div>
    <p class="brand-name">Cedar Pike</p>
    <ul class="contact">
      <li>
        <svg width="14" height="14" viewBox="0 0 22 22" aria-hidden="true">
          <rect x="1" y="1" width="20" height="20" fill="none" stroke="var(--white)" stroke-width="2"/>
          <path d="M7 5 l2 0 l1 3 l-1.5 1 a7 7 0 0 0 3.5 3.5 l1 -1.5 l3 1 l0 2 a2 2 0 0 1 -2 1.5 a10 10 0 0 1 -8.5 -8.5 a2 2 0 0 1 1.5 -2z" fill="var(--white)"/>
        </svg>
        <span>318.555.0147</span>
      </li>
      <li>
        <svg width="14" height="14" viewBox="0 0 22 22" aria-hidden="true">
          <rect x="1" y="1" width="20" height="20" fill="none" stroke="var(--white)" stroke-width="2"/>
          <circle cx="11" cy="11" r="6" fill="none" stroke="var(--white)" stroke-width="1.5"/>
          <ellipse cx="11" cy="11" rx="2.5" ry="6" fill="none" stroke="var(--white)" stroke-width="1.2"/>
          <line x1="5" y1="11" x2="17" y2="11" stroke="var(--white)" stroke-width="1.2"/>
        </svg>
        <span>cedarpikeco.com</span>
      </li>
    </ul>
  </section>

</main>
</body>
</html>
```